Tides of the barrio "Las mareas del barrio nuevo"

I'm writing a book about word of mouth and the consumer as the media "the book is in Spanish" so you have to use "Las mareas del barrio nuevo" the subtitle is and 30 examples that proves it "Con doce relatos de esquina"

Book is about the power of consumer nowadays , the book will combine the era of social media but also the power of one to one word of mouth meaning w/o being connected to an electronic platform

Tides of the new barrio is a book about the power that now the consumer has in this double way interaction between the brands and the consumer, between the services and the people between the social media and the traditional media.

Consumer is on control and it is because "tides of the new barrio"

About book principles
I love simple books white background, simplicity around the fonts and the images (simple is better)

Target Market(s)

Marketing and digital marketing managers, social media managers, community managers, social media agencies, business people

Industry/Entity Type

Electronic

Requirements
Must have
• White backgroung, black and red fonts big fonts
Nice to have
• the subtitle "Con doce relatos de la calle"

```html
<!DOCTYPE html>
<html lang="es">
<head>
<meta charset="utf-8">
<title>Las mareas del barrio nuevo — cubierta</title>
<link rel="stylesheet" href="https://fonts.googleapis.com/css2?family=Josefin+Sans:wght@400;600;700&family=Open+Sans:wght@700&display=swap">
<style>
  :root {
    --stage: #ececec;
    --paper: #f7f7f7;
    --paper-back: #ececec;
    --ink: #1a1a1a;
    --accent-red: #c8141e;
    --band: #111111;
    --band-text: #ffffff;
    --photo-light: #f2f2f2;
    --photo-mid: #cfcfcf;
    --photo-dark: #2a2a2a;
  }
  * { box-sizing: border-box; margin: 0; padding: 0; }
  html, body { width: 1200px; height: 800px; overflow: hidden; }
  body {
    background: var(--stage);
    font-family: "Josefin Sans", "Helvetica Neue", sans-serif;
    color: var(--ink);
  }
  .cover-wrap {
    position: absolute;
    left: 163px; top: 90px;
    display: flex;
    height: 620px;
    box-shadow: 0 10px 30px rgba(0,0,0,0.12);
  }
  /* Back cover */
  .back-cover {
    width: 420px; height: 100%;
    background: var(--paper-back);
    padding: 18px 26px 26px;
    display: flex; flex-direction: column;
  }
  .back-author {
    align-self: flex-end;
    font-weight: 700; font-size: 13px; letter-spacing: 0.5px;
    text-transform: uppercase;
  }
  .back-title { font-weight: 600; }
  .back-title .line-small { font-size: 27px; line-height: 1; margin-top: 6px; }
  .back-title .line-big { font-size: 41px; line-height: 1.05; }
  .back-subtitle {
    font-size: 15px; font-weight: 700; letter-spacing: 0.6px;
    text-transform: uppercase; margin-top: 10px;
    color: var(--accent-red);
  }
  .back-blurb {
    font-family: "Open Sans", Arial, sans-serif;
    font-weight: 700; font-size: 9.4px; line-height: 1.52;
    text-align: justify; text-align-last: center;
    margin-top: 18px;
  }
  .back-boxes {
    margin-top: auto;
    display: flex; justify-content: space-between;
  }
  .back-box {
    width: 112px; height: 52px;
    background: var(--band); color: var(--band-text);
    font-size: 11px; font-weight: 400; letter-spacing: 0.5px;
    display: flex; align-items: center; justify-content: center;
  }
  /* Spine */
  .spine {
    width: 34px; height: 100%;
    background: linear-gradient(90deg, #dcdcdc, #f4f4f4 50%, #dcdcdc);
    display: flex; flex-direction: column; align-items: center;
    padding: 18px 0 22px;
  }
  .spine-title {
    writing-mode: vertical-rl;
    font-size: 26px; font-weight: 600; letter-spacing: 1.5px;
    text-transform: uppercase; line-height: 1;
  }
  .spine-title small { font-size: 17px; }
  .spine-title .spine-accent { color: var(--accent-red); }
  .spine-author {
    writing-mode: vertical-rl; margin-top: auto;
    font-size: 10px; font-weight: 700; letter-spacing: 1px;
    text-transform: uppercase;
  }
  /* Front cover */
  .front-cover {
    width: 420px; height: 100%;
    background: var(--paper);
    position: relative;
    padding: 34px 20px 0 26px;
  }
  .front-title { font-weight: 600; }
  .front-title .line-small {
    font-size: 32px; line-height: 1;
    text-shadow: 1px 1px 0 rgba(0,0,0,0.15);
  }
  .front-title .line-big {
    font-size: 47px; line-height: 1.1;
    text-shadow: 1px 1px 0 rgba(0,0,0,0.15);
  }
  .front-subtitle {
    font-size: 17px; font-weight: 700; letter-spacing: 0.8px;
    text-transform: uppercase; margin-top: 16px;
    color: var(--accent-red);
  }
  .cover-photo {
    position: absolute; left: 50px; right: 20px; top: 300px; height: 272px;
  }
  .author-band {
    position: absolute; left: 0; right: 0; bottom: 14px; height: 36px;
    background: var(--band); color: var(--band-text);
    display: flex; align-items: center; justify-content: center;
    font-size: 13px; font-weight: 700; letter-spacing: 1px;
    text-transform: uppercase;
  }
</style>
</head>
<body>
  <main class="cover-wrap">
    <section class="back-cover">
      <p class="back-author">Tomás Echeverri</p>
      <h2 class="back-title">
        <div class="line-small">LAS MAREAS DEL</div>
        <div class="line-big">BARRIO NUEVO</div>
      </h2>
      <p class="back-subtitle">Con doce relatos de esquina</p>
      <p class="back-blurb">Lorem ipsum dolor sit amet, consectetur adipisicing elit, sed do eiusmod tempor incididunt ut labore et dolore magna aliqua. Ut enim ad minim veniam, quis nostrud exercitation. Lorem ipsum dolor sit amet, consectetur adipisicing elit, sed do eiusmod tempor incididunt ut labore et dolore magna aliqua. Ut enim ad minim veniam, quis nostrud exercitation. Lorem ipsum dolor sit amet, consectetur adipisicing elit, sed do eiusmod tempor incididunt ut labore et dolore magna aliqua. Ut enim ad minim veniam, quis nostrud exercitation. Lorem ipsum dolor sit amet, consectetur adipisicing elit, sed do eiusmod tempor incididunt ut labore et dolore magna aliqua. Ut enim ad minim veniam, quis nostrud exercitation. Lorem ipsum dolor sit amet, consectetur adipisicing elit, sed do eiusmod tempor incididunt ut labore et dolore magna aliqua. Ut enim ad minim veniam, quis nostrud exercitation. Lorem ipsum dolor sit amet, consectetur adipisicing elit, sed do eiusmod tempor incididunt ut labore et dolore magna aliqua. Ut enim ad minim veniam, quis nostrud exercitation. Lorem ipsum dolor sit amet, consectetur adipisicing elit, sed do eiusmod tempor incididunt ut labore et dolore magna aliqua. Ut enim ad minim veniam, quis nostrud exercitation.</p>
      <div class="back-boxes">
        <div class="back-box">LOGO</div>
        <div class="back-box">ISBN</div>
      </div>
    </section>

    <section class="spine">
      <p class="spine-title"><small>LAS</small> MAREAS <small>DEL</small> <span class="spine-accent">BARRIO NUEVO</span></p>
      <p class="spine-author">Tomás Echeverri</p>
    </section>

    <section class="front-cover">
      <h1 class="front-title">
        <div class="line-small">LAS MAREAS DEL</div>
        <div class="line-big">BARRIO NUEVO</div>
      </h1>
      <p class="front-subtitle">Con doce relatos de esquina</p>
      <svg class="cover-photo" viewBox="0 0 350 272" preserveAspectRatio="none" role="img"
           aria-label="Fotografía: mujer sentada ante un ordenador de cuyo monitor sale una mano entregándole bolsas de compras de colores">
        <defs>
          <linearGradient id="photoTone" x1="0" y1="0" x2="1" y2="1">
            <stop offset="0" stop-color="var(--photo-light)"/>
            <stop offset="0.55" stop-color="var(--photo-mid)"/>
            <stop offset="1" stop-color="var(--photo-dark)"/>
          </linearGradient>
        </defs>
        <rect width="350" height="272" fill="url(#photoTone)" opacity="0.55"/>
      </svg>
      <div class="author-band">Tomás Echeverri</div>
    </section>
  </main>
</body>
</html>
```